BEACON CABS

Taxi card design

Need changes very slow in replying to my messages.

Target Market(s)

Customers

Industry/Entity Type

Taxi

Contact Information for Business Card

See previous design

Font styles to use
Sans Serif

Colors
A7469A
B969AE
D3A5CF
EDDBEB
F8F0F9
6B429C
8869AF
B7A5CE
E3DAEB
F3F0F8

Requirements
Nice to have
• We are in the business of looking after people, not just driving vehicles front
Should not have
• Front number 01632 480 480 needs to big big

```html
<!DOCTYPE html>
<html lang="en">
<head>
<meta charset="utf-8">
<title>Beacon Cabs – Business Card</title>
<link href="https://fonts.googleapis.com/css2?family=Arimo:wght@400;700&family=Exo+2:wght@800&display=swap" rel="stylesheet">
<style>
  :root {
    --bg: #1c1c1e;
    --card: #0c0b0d;
    --card-edge: #19171b;
    --purple-deep: #6b429c;
    --purple-mid: #8869af;
    --magenta: #a7469a;
    --magenta-light: #b969ae;
    --text: #ffffff;
    --muted: #d3d0d6;
  }
  * { margin: 0; padding: 0; box-sizing: border-box; }
  html, body { width: 1200px; height: 900px; overflow: hidden; }
  body {
    background: var(--bg);
    font-family: "Arimo", Arial, sans-serif;
    color: var(--text);
    position: relative;
  }
  .card {
    position: absolute;
    top: 269px;
    width: 560px;
    height: 362px;
    border-radius: 22px;
    background: radial-gradient(ellipse at 70% 20%, var(--card-edge), var(--card) 70%);
    box-shadow: 0 14px 40px rgba(0,0,0,.6);
    overflow: hidden;
  }
  .card--front { left: 30px; }
  .card--back { left: 610px; }

  .brand {
    display: flex; align-items: center; gap: 12px;
    font-family: "Arimo", Arial, sans-serif;
    font-weight: 700;
    color: var(--text);
    letter-spacing: 1px;
  }
  .brand__mark { width: 16px; height: 16px; background: var(--magenta); border-radius: 3px; }

  /* front */
  .card--front .brand { position: absolute; left: 60px; top: 44px; font-size: 46px; }
  .rule { position: absolute; left: 0; width: 100%; height: 2px; background: linear-gradient(90deg, var(--purple-deep), var(--magenta)); }
  .card--front .rule--top { top: 120px; }
  .card--front .rule--bottom { top: 222px; }
  .hero-phone {
    position: absolute; left: 40px; top: 138px;
    display: flex; align-items: center; gap: 16px;
  }
  .hero-phone__number {
    font-family: "Exo 2", sans-serif; font-weight: 800;
    font-size: 52px; letter-spacing: 2px;
    background: linear-gradient(90deg, var(--purple-deep), var(--magenta-light));
    -webkit-background-clip: text; background-clip: text; color: transparent;
  }
  .icon {
    width: 22px; height: 22px; flex: none;
    background: linear-gradient(135deg, var(--magenta), var(--purple-deep));
    border-radius: 3px; display: flex; align-items: center; justify-content: center;
  }
  .icon--large { width: 36px; height: 36px; }
  .icon svg { width: 70%; height: 70%; }
  .contact { display: flex; align-items: center; gap: 9px; font-size: 16px; line-height: 1; white-space: nowrap; }
  .phones-row {
    position: absolute; left: 40px; top: 200px; width: 500px;
    display: flex; justify-content: space-between; display: none;
  }
  .contact-grid {
    position: absolute; left: 40px; top: 238px; right: 30px;
    display: grid; grid-template-columns: 1fr 1fr; gap: 12px 18px;
  }
  .contact-list { display: flex; flex-direction: column; gap: 10px; }
  .contact__label { color: var(--magenta-light); }
  .address { display: flex; gap: 9px; font-size: 16px; line-height: 1.25; }

  /* back */
  .card--back .brand { position: absolute; left: 0; right: 0; top: 118px; justify-content: center; font-size: 52px; }
  .tagline { position: absolute; right: 92px; top: 186px; font-size: 15px; color: var(--muted); }
  .card--back .rule--top { top: 238px; }
  .card--back .rule--bottom { top: 290px; }
  .services {
    position: absolute; left: 0; right: 0; top: 253px;
    display: flex; justify-content: center; align-items: center; gap: 12px;
    font-size: 20px;
  }
  .services__dot { width: 8px; height: 8px; border-radius: 50%; background: var(--magenta); }
</style>
</head>
<body>

<section class="card card--front">
  <div class="brand"><span class="brand__mark"></span>BEACON CABS</div>
  <div class="rule rule--top"></div>
  <div class="hero-phone">
    <span class="icon icon--large"><svg viewBox="0 0 24 24"><path fill="#fff" d="M6.6 10.8a15 15 0 0 0 6.6 6.6l2.2-2.2c.3-.3.7-.4 1-.2 1.1.4 2.3.6 3.6.6.6 0 1 .4 1 1V20c0 .6-.4 1-1 1A17 17 0 0 1 3 4c0-.6.4-1 1-1h3.5c.6 0 1 .4 1 1 0 1.3.2 2.5.6 3.6.1.3 0 .7-.2 1z"/></svg></span>
    <span class="hero-phone__number">01632 480 480</span>
  </div>
  <div class="rule rule--bottom"></div>

  <div class="contact-grid">
    <div class="contact-list">
      <div class="contact"><span class="icon"><svg viewBox="0 0 24 24"><path fill="#fff" d="M6.6 10.8a15 15 0 0 0 6.6 6.6l2.2-2.2c.3-.3.7-.4 1-.2 1.1.4 2.3.6 3.6.6.6 0 1 .4 1 1V20c0 .6-.4 1-1 1A17 17 0 0 1 3 4c0-.6.4-1 1-1h3.5c.6 0 1 .4 1 1 0 1.3.2 2.5.6 3.6.1.3 0 .7-.2 1z"/></svg></span>01632 960 166</div>
      <div class="contact"><span class="icon"><svg viewBox="0 0 24 24"><path fill="#fff" d="M6.6 10.8a15 15 0 0 0 6.6 6.6l2.2-2.2c.3-.3.7-.4 1-.2 1.1.4 2.3.6 3.6.6.6 0 1 .4 1 1V20c0 .6-.4 1-1 1A17 17 0 0 1 3 4c0-.6.4-1 1-1h3.5c.6 0 1 .4 1 1 0 1.3.2 2.5.6 3.6.1.3 0 .7-.2 1z"/></svg></span><span><span class="contact__label">Freephone:</span> 0808 157 0222</span></div>
      <div class="contact"><span class="icon"><svg viewBox="0 0 24 24"><path fill="none" stroke="#fff" stroke-width="2" d="M3 6h18v12H3z M3 6l9 7 9-7"/></svg></span>hello@beaconcabs.co.uk</div>
      <div class="contact"><span class="icon"><svg viewBox="0 0 24 24"><g fill="none" stroke="#fff" stroke-width="1.8"><circle cx="12" cy="12" r="9"/><path d="M3 12h18M12 3c3 3 3 15 0 18M12 3c-3 3-3 15 0 18"/></g></svg></span>www.beaconcabs.co.uk</div>
    </div>
    <div class="contact-list">
      <div class="contact"><span class="icon"><svg viewBox="0 0 24 24"><path fill="#fff" d="M6.6 10.8a15 15 0 0 0 6.6 6.6l2.2-2.2c.3-.3.7-.4 1-.2 1.1.4 2.3.6 3.6.6.6 0 1 .4 1 1V20c0 .6-.4 1-1 1A17 17 0 0 1 3 4c0-.6.4-1 1-1h3.5c.6 0 1 .4 1 1 0 1.3.2 2.5.6 3.6.1.3 0 .7-.2 1z"/></svg></span>01632 960 202</div>
      <div class="contact"><span class="icon"><svg viewBox="0 0 24 24"><path fill="#fff" d="M6.6 10.8a15 15 0 0 0 6.6 6.6l2.2-2.2c.3-.3.7-.4 1-.2 1.1.4 2.3.6 3.6.6.6 0 1 .4 1 1V20c0 .6-.4 1-1 1A17 17 0 0 1 3 4c0-.6.4-1 1-1h3.5c.6 0 1 .4 1 1 0 1.3.2 2.5.6 3.6.1.3 0 .7-.2 1z"/></svg></span>01632 960 811</div>
      <div class="address"><span class="icon"><svg viewBox="0 0 24 24"><path fill="#fff" d="M12 2a7 7 0 0 0-7 7c0 5 7 13 7 13s7-8 7-13a7 7 0 0 0-7-7zm0 9.5a2.5 2.5 0 1 1 0-5 2.5 2.5 0 0 1 0 5z"/></svg></span><span>Beacon Hall,<br>Mill Lane Northbridge<br>NB4 2QT</span></div>
    </div>
  </div>
</section>

<section class="card card--back">
  <div class="brand"><span class="brand__mark"></span>BEACON CABS</div>
  <div class="tagline">24/7 service</div>
  <div class="rule rule--top"></div>
  <div class="services">
    <span>Airport Transfers</span><span class="services__dot"></span>
    <span>Minibuses</span><span class="services__dot"></span>
    <span>School Transport</span>
  </div>
  <div class="rule rule--bottom"></div>
</section>

</body>
</html>
```